Venture Capital Firm needs new Business Cards

We need a business card design for "Stonebrook Partners". We already have a logo which we are happy with - we now need to have business cards designed.
Stonebrook is a venture capital firm, which means that we look to invest in technology start-ups. See our website www.stonebrookpx.example for more details.
Updates
Project Deadline Extended Reason: Apologies for not being very responsive. Will push back the deadline a couple days in order to give feedback and allow other people to present designs. Added Wednesday, October 22, 2014
Industry/Entity Type
Business
Look and feel
Each slider illustrates characteristics of the customer's brand and the style your logo design should communicate.

```html
<!DOCTYPE html>
<html lang="en">
<head>
<meta charset="utf-8">
<title>Stonebrook Partners – Business Cards</title>
<link href="https://fonts.googleapis.com/css2?family=Abel&display=swap" rel="stylesheet">
<style>
  :root {
    --backdrop: #2b2b2b;
    --card-white: #ffffff;
    --brand-blue: #3349a0;
    --logo-navy: #2f3c96;
    --pattern-light: #d7ecf6;
    --pattern-mid: #9fd0ea;
    --muted-grey: #6f7378;
    --ink-white: #ffffff;
  }
  * { box-sizing: border-box; margin: 0; padding: 0; }
  html, body {
    width: 968px;
    height: 1200px;
    overflow: hidden;
    background: var(--backdrop);
    font-family: "Abel", sans-serif;
  }
  .sheet {
    position: relative;
    width: 968px;
    height: 1200px;
  }
  .card {
    position: absolute;
    left: 48px;
    width: 872px;
    height: 500px;
    box-shadow: 0 10px 30px rgba(0,0,0,0.45);
    overflow: hidden;
  }

  /* Front */
  .card-front {
    top: 70px;
    background: var(--card-white);
  }
  .tree-pattern {
    position: absolute;
    inset: 0;
    background: linear-gradient(135deg, var(--pattern-light), var(--pattern-mid) 50%, var(--pattern-light));
  }
  .front-logo-panel {
    position: absolute;
    left: 281px;
    top: 160px;
    width: 310px;
    height: 180px;
    background: var(--card-white);
    display: flex;
    flex-direction: column;
    align-items: center;
    justify-content: center;
    color: var(--logo-navy);
  }
  .front-logo-panel .wordmark { font-size: 58px; line-height: 1; }
  .front-logo-panel .wordmark-sub {
    font-size: 20px;
    letter-spacing: 7px;
    margin-top: 8px;
    color: var(--logo-navy);
  }

  /* Back */
  .card-back {
    top: 630px;
    background: var(--brand-blue);
    color: var(--ink-white);
  }
  .back-logo {
    position: absolute;
    left: 50px;
    top: 44px;
    display: flex;
    align-items: center;
    gap: 18px;
  }
  .logo-dot {
    width: 46px;
    height: 46px;
    border-radius: 50%;
    background: var(--ink-white);
  }
  .back-logo .wordmark { font-size: 62px; line-height: 1; }
  .back-logo .wordmark-sub {
    font-size: 20px;
    letter-spacing: 8px;
    margin-top: 4px;
    padding-left: 40px;
  }
  .person {
    position: absolute;
    left: 220px;
    top: 215px;
    text-align: right;
    width: 200px;
  }
  .person-name { font-size: 40px; }
  .person-role { font-size: 28px; margin-top: 8px; }
  .divider {
    position: absolute;
    left: 460px;
    top: 200px;
    width: 8px;
    height: 200px;
    border-left: 1.5px solid rgba(255,255,255,0.8);
    border-right: 1.5px solid rgba(255,255,255,0.8);
  }
  .contacts {
    position: absolute;
    left: 505px;
    top: 150px;
    list-style: none;
  }
  .contact {
    display: flex;
    align-items: flex-start;
    gap: 22px;
    margin-bottom: 24px;
    font-size: 26px;
    line-height: 1.25;
  }
  .contact svg {
    width: 42px;
    height: 42px;
    flex: none;
    stroke: var(--ink-white);
    fill: none;
    stroke-width: 2.5;
  }
  .contact .text { padding-top: 6px; }
</style>
</head>
<body>
<main class="sheet">

  <section class="card card-front" aria-label="Business card front">
    <div class="tree-pattern" role="img" aria-label="Repeating pattern of small blue stylised trees covering the card"></div>
    <div class="front-logo-panel">
      <span class="wordmark">Stonebrook</span>
      <span class="wordmark-sub">PARTNERS</span>
    </div>
  </section>

  <section class="card card-back" aria-label="Business card back">
    <div class="back-logo">
      <span class="logo-dot"></span>
      <div>
        <div class="wordmark">Stonebrook</div>
        <div class="wordmark-sub">PARTNERS</div>
      </div>
    </div>

    <div class="person">
      <p class="person-name">Daniel Harper</p>
      <p class="person-role">Director</p>
    </div>

    <div class="divider"></div>

    <ul class="contacts">
      <li class="contact">
        <svg viewBox="0 0 40 40" aria-hidden="true">
          <circle cx="20" cy="20" r="17"/>
          <ellipse cx="20" cy="20" rx="8" ry="17"/>
          <line x1="3" y1="20" x2="37" y2="20"/>
          <line x1="20" y1="3" x2="20" y2="37"/>
          <path d="M6 11h28M6 29h28"/>
        </svg>
        <span class="text">www.stonebrookpx.example</span>
      </li>
      <li class="contact">
        <svg viewBox="0 0 40 40" aria-hidden="true">
          <rect x="3" y="8" width="34" height="24" rx="2"/>
          <path d="M3 9l17 13 17-13"/>
        </svg>
        <span class="text">info@stonebrookpx.example</span>
      </li>
      <li class="contact">
        <svg viewBox="0 0 40 40" aria-hidden="true">
          <path d="M4 14c0-5 32-5 32 0v3h-8v-3H12v3H4z" fill="#fff"/>
          <path d="M12 19h16l5 15H7z" fill="#fff"/>
          <circle cx="20" cy="27" r="4" stroke="#3349a0"/>
        </svg>
        <span class="text">360-41-275</span>
      </li>
      <li class="contact">
        <svg viewBox="0 0 40 40" aria-hidden="true">
          <path d="M4 20L20 5l16 15"/>
          <path d="M8 17v19h24V17"/>
          <rect x="14" y="22" width="12" height="8"/>
          <line x1="16" y1="26" x2="24" y2="26"/>
        </svg>
        <span class="text">48 Harbour Lane<br>Westmere, NSW, 2999,<br>Australia</span>
      </li>
    </ul>
  </section>

</main>
</body>
</html>
```